Buch-/E-Book-Cover zum Thema Veltra Code
Zielgruppe
Hallo lieber Designer,
ich arbeite an einem Buch zum Thema Veltra Code. Dies ist ein System der Persönlichkeitsentwicklung.
Die Zielgruppe sind also Männer und Frauen mittleren Alters, die nach spiritueller Erfüllung und Selbsterkenntnis streben. Das Buchcover sollte dementsprechend esoterisch und meditativ angehaucht, aber trotzdem klar und modern strukturiert sein.
Du kannst dich gerne bei schon bestehenden Buchdesigns inspirieren lassen (Veltra Code Bücher auf Bücherkai)!
Die Zeichnung der sitzenden Menschen auf den Covern nennen sich Body Chart, falls du es für dein Design brauchst.
Ich habe aber extra nicht an den Reglern unten geschoben, damit du deine Kreativität ausleben kannst.
Aufgabenstellung
Der Auftrag beinhaltet die Buchvorderseite, die Rückseite UND den Buchrücken (die Spine). Deswegen habe ich das Preisgeld angehoben.
Vorder- und Rückseite haben ein Format von 6*9 Zoll, also 6 Zoll breit und 9 Zoll hoch. Der Buchrücken ist 0,338 Zoll breit und ebenfalls 9 Zoll hoch. Ich habe eine PNG-Datei angehängt, die das Ganze noch einmal visualisiert. Es wäre gut, wenn du dein Design dann auch in der gleichen Konstellation hochlädst (Rückseite, Rücken, Vorderseite). Außerdem braucht das Design an jeder Außenseite eine Beschnittzugabe von 0,125 Zoll. Deswegen ist die Gesamtdatei 12,533 * 9,25 Zoll groß. Auf dieser Beschnittzugabe kann das Design gerne noch weitergehen, damit keine unsauberen Bereiche beim Beschneiden entstehen. Es sollte aber kein Text mehr darauf vorhanden sein.
Vorderseite:
Titel: 'Veltra Code – Das Kleine Nordlicht 40 Schritte durch alte Muster im Veltra Code Modell für mehr Ruhe im Alltag und einen klaren Blick auf die eigene innere Mitte'
• Muss komplett und in Gänze vorne auf dem Buchcover drauf sein
• Highlight auf „Veltra Code – Das Kleine Nordlicht“
• Den Rest des Titels in kleinerer Schrift, aber trotzdem auf dem Cover
Autorenname: Jonas Kreuder
• Auch etwas größer als der Nebentitel
Buchrücken (Spine):
• nur „Veltra Code - Das Kleine Nordlicht“ (nicht den restlichen Titel) und den Namen des Autors
Rückseite:
Klappentext:
'Gehe auf die Reise zu Deinem wahren Ich
Beim Veltra-Code-Modell geht es um die Persönlichkeit und die individuelle Weiterentwicklung. Die Zielsetzung besteht darin, jedem Menschen zu ermöglichen, ein erfolgreiches, selbstbestimmtes und erfülltes Leben zu führen. Um dieses Ziel zu erreichen, ist es wichtig, die eigenen Stärken und Schwächen sowie die im Geburtshoroskop festgelegten Persönlichkeitsstrukturen zu kennen und zu berücksichtigen.
Dieses einzigar..

```html
<!DOCTYPE html>
<html lang="de">
<head>
<meta charset="utf-8">
<title>Veltra Code – Das Kleine Nordlicht · Buchumschlag</title>
<link href="https://fonts.googleapis.com/css2?family=Bebas+Neue&family=Francois+One&family=Roboto:wght@400;500&display=swap" rel="stylesheet">
<style>
  :root {
    --orange-deep: #b8400f;
    --orange-mid: #d95a1d;
    --orange-light: #ec8a3c;
    --orange-glow: #f29a48;
    --ink: #1a0d07;
    --white: #ffffff;
  }
  * { margin: 0; padding: 0; box-sizing: border-box; }
  html, body { width: 1200px; height: 882px; overflow: hidden; }
  body { font-family: "Roboto", sans-serif; color: var(--white); }

  .cover {
    position: relative;
    width: 1200px;
    height: 882px;
    overflow: hidden;
    background:
      radial-gradient(ellipse 420px 300px at 300px 380px, rgba(242,154,72,.55), transparent 70%),
      radial-gradient(ellipse 380px 260px at 880px 640px, rgba(236,138,60,.45), transparent 70%),
      radial-gradient(ellipse 500px 260px at 200px 820px, rgba(184,64,15,.6), transparent 70%),
      radial-gradient(ellipse 300px 200px at 1100px 120px, rgba(184,64,15,.5), transparent 70%),
      radial-gradient(ellipse 260px 200px at 620px 500px, rgba(160,50,10,.35), transparent 70%),
      linear-gradient(160deg, var(--orange-mid), var(--orange-deep) 55%, var(--orange-mid));
  }

  /* Rückseite */
  .back { position: absolute; left: 61px; top: 72px; width: 490px; }
  .back-headline {
    font-family: "Francois One", sans-serif;
    font-size: 41px;
    line-height: 50px;
    font-weight: 400;
    margin-bottom: 16px;
  }
  .back-blurb p {
    font-size: 16.4px;
    line-height: 25.4px;
    margin-bottom: 25.4px;
  }

  /* Buchrücken */
  .spine {
    position: absolute;
    left: 599px;
    top: 441px;
    transform: translate(-50%, -50%) rotate(-90deg);
    white-space: nowrap;
    font-size: 15px;
    font-weight: 500;
    letter-spacing: 1.3px;
    text-transform: uppercase;
  }
  .spine-author { margin-right: 26px; }

  /* Vorderseite */
  .front-title { position: absolute; left: 650px; top: 40px; }
  .front-title text { font-family: "Bebas Neue", sans-serif; fill: var(--white); }
  .front-subtitle {
    position: absolute;
    left: 641px;
    width: 500px;
    top: 421px;
    text-align: center;
    font-size: 19px;
    line-height: 24px;
    letter-spacing: .2px;
  }
  .body-chart-art {
    position: absolute;
    left: 741px;
    top: 501px;
    width: 306px;
    height: 308px;
  }
  .front-author {
    position: absolute;
    left: 0; right: 0;
    margin-left: 641px;
    width: 522px;
    top: 820px;
    text-align: center;
    font-size: 28px;
    font-weight: 500;
    letter-spacing: 2.4px;
  }
</style>
</head>
<body>
<main class="cover">

  <section class="back">
    <h2 class="back-headline">Gehe auf die Reise<br>zu Deinem wahren Ich</h2>
    <div class="back-blurb">
      <p>Beim Veltra-Code-Modell geht es um die Persönlichkeit und die individuelle Weiterentwicklung. Die Zielsetzung besteht darin, jedem Menschen zu ermöglichen, ein erfolgreiches, selbstbestimmtes und erfülltes Leben zu führen.</p>
      <p>Um dieses Ziel zu erreichen, ist es wichtig, die eigenen Stärken und Schwächen sowie die im Geburtshoroskop festgelegten Persönlichkeitsstrukturen zu kennen und zu berücksichtigen.</p>
      <p>Dieses einzigartige System verbindet bewährte Traditionen und moderne Wissenschaften miteinander. Anhand Ihrer seelischen Landkarte werden individuelle Charaktereigenschaften und deren Auswirkungen auf den Lauf Ihres Lebens aufgezeigt. Es hilft dabei, Selbstakzeptanz und Selbstliebe zu entwickeln.</p>
    </div>
  </section>

  <div class="spine">
    <span class="spine-author">Jonas Kreuder</span>
    <span class="spine-title">Veltra Code - Das Kleine Nordlicht</span>
  </div>

  <svg class="front-title" width="490" height="380" viewBox="0 0 490 380" aria-label="Veltra Code – Das Kleine Nordlicht">
    <text x="0" y="156" font-size="214" textLength="488" lengthAdjust="spacingAndGlyphs">VELTRA</text>
    <text x="0" y="313" font-size="214" textLength="488" lengthAdjust="spacingAndGlyphs">CODE</text>
    <text x="3" y="374" font-size="64" textLength="482" lengthAdjust="spacingAndGlyphs">DAS KLEINE NORDLICHT</text>
  </svg>

  <p class="front-subtitle">40 Schritte durch alte Muster im Veltra Code Modell für mehr Ruhe im Alltag und einen klaren Blick auf die eigene innere Mitte</p>

  <svg class="body-chart-art" viewBox="0 0 306 308" role="img" aria-label="Body Chart einer sitzenden Figur vor einem Mandala in Schwarz und Orange">
    <defs>
      <radialGradient id="chartTone" cx="50%" cy="55%" r="50%">
        <stop offset="0" stop-color="#3a1a0a"/>
        <stop offset=".7" stop-color="#1a0d07"/>
        <stop offset="1" stop-color="#1a0d07" stop-opacity="0"/>
      </radialGradient>
    </defs>
    <ellipse cx="153" cy="160" rx="153" ry="148" fill="url(#chartTone)"/>
  </svg>

  <p class="front-author">JONAS KREUDER</p>

</main>
</body>
</html>
```